Adult Flushable Wipes Product Packaging design

We are launching an adult flushable wipe and we require a logo & product packaging design.

The brand is called: Velvet Valet

The wipe will be slightly upmarket and will sell mainly online. The branding should be funny but still professional. It's intended audience is men between 18-45 and it will be used as a body cleansing wipe.

for general body cleaning
-bathroom/toilet wipes
-grooming wipes
-refreshing wipes

Target Market(s)

Men Ages 18-45

Font styles to use
Decorative

Colors
86cfc6
33b8a4
85cae6
33a6d7

Requirements
Must have
• there are 50 wipes per pack. this should be incorporated in the design.
• the wipes are 5.9" x 7.9" this should be incorporated in the design.
• the wipes have a fragrance which we will call the "Velvet Breeze" this should be incorporated in the design.
Nice to have
• We like the idea of incorporating a butler/tuxedo into the product design. lots of black/white with a matte finish and can also have some silver.
Should not have
• too many colours. we want a simple design

```html
<!DOCTYPE html>
<html lang="en">
<head>
<meta charset="utf-8">
<title>Velvet Valet Adult Wipes – Pack Front</title>
<link href="https://fonts.googleapis.com/css2?family=Bebas+Neue&family=Mulish:wght@400;500&display=swap" rel="stylesheet">
<style>
  :root {
    --backdrop: #dcdcdc;
    --pack-black: #0b0b0b;
    --pack-white: #e9e9e9;
    --ink: #1c1c1c;
    --light-text: #ffffff;
  }
  html, body {
    margin: 0;
    padding: 0;
    overflow: hidden;
  }
  body {
    width: 857px;
    height: 1200px;
    background: var(--backdrop);
  }
  .canvas {
    position: relative;
    width: 857px;
    height: 1200px;
  }
  .pack-shape,
  .emblem-area {
    position: absolute;
    left: 0;
    top: 0;
  }
  .tagline,
  .wipe-count,
  .wipe-size {
    position: absolute;
    left: 0;
    width: 857px;
    margin: 0;
    text-align: center;
    font-family: "Mulish", sans-serif;
    font-weight: 400;
    color: var(--light-text);
    line-height: 1;
  }
  .tagline {
    top: 257px;
    left: 14px;
    font-size: 25px;
    letter-spacing: 0.3px;
  }
  .wipe-count {
    top: 963px;
    left: 4px;
    font-size: 25px;
  }
  .wipe-size {
    top: 999px;
    left: 4px;
    font-size: 24px;
  }
  .label-pill {
    position: absolute;
    height: 52px;
    box-sizing: border-box;
    border: 3px solid var(--light-text);
    border-radius: 26px;
    background: var(--pack-black);
    outline: 3px solid var(--pack-black);
    color: var(--light-text);
    font-family: "Bebas Neue", sans-serif;
    font-size: 40px;
    line-height: 48px;
    letter-spacing: 3px;
    text-align: center;
  }
  .category-pill {
    left: 272px;
    top: 309px;
    width: 332px;
  }
  .scent-pill {
    left: 280px;
    top: 874px;
    width: 332px;
  }
  .brand-name {
    position: absolute;
    top: 396px;
    left: 0;
    width: 895px;
    margin: 0;
    text-align: center;
    font-family: "Bebas Neue", sans-serif;
    font-weight: 400;
    font-size: 78px;
    line-height: 1;
    letter-spacing: 1px;
    color: var(--ink);
  }
</style>
</head>
<body>
  <main class="canvas">
    <svg class="pack-shape" width="857" height="1200" viewBox="0 0 857 1200" aria-hidden="true">
      <rect class="pack-body" x="100" y="72" width="687" height="1086" rx="6" fill="var(--pack-black)"/>
      <path class="pack-window"
            d="M100 400 Q443 320 787 405 L787 840 Q443 910 100 842 Z"
            fill="var(--pack-white)"/>
    </svg>

    <svg class="emblem-area" width="857" height="1200" viewBox="0 0 857 1200"
         role="img" aria-label="Tuxedo and bow tie emblem in black on white">
      <circle cx="448" cy="664" r="184" fill="var(--pack-black)"/>
    </svg>

    <p class="tagline">Hypoallergenic for Sensitive Skin</p>
    <div class="label-pill category-pill">Adult Wipes</div>
    <h1 class="brand-name">Velvet Valet</h1>
    <div class="label-pill scent-pill">Velvet Breeze</div>
    <p class="wipe-count">50 Antibacterial Wipes</p>
    <p class="wipe-size">(Size : 5.9″ x 7.9″)</p>
  </main>
</body>
</html>
```